Pat Greene Billboard

**Task Description: Billboard Design for Self Storage Facility**

**Objective:**
Design a captivating billboard to promote our self-storage facility with a focus on our convenient location and online rental capabilities.

**Key Messages to Include:**
1. **Location Emphasis:** Highlight that our facility is located right beside the billboard (maybe by using an arrow pointing left).
2. **Online Rental Convenience:** Feature prominently that customers can "Rent Online Anytime!” or that we are "Always Open Online!"

**Target Audience:**
- Local residents looking for convenient self-storage solutions.
- Businesses needing storage space accessible around the clock.

**Design Elements:**
1. **Visual Impact:** Eye-catching graphics and colors that stand out against the surroundings.
2. **Clear Text:** Bold and concise messaging that can be read and understood quickly.
3. **Contact Information:** Include our phone number and website URL for easy access to further information.

**Additional Information:**
- Billboard dimensions: 12 ft. x 24 ft.
- Preferred color scheme: Bright and attention-grabbing, but professional.
- Branding: Incorporate our logo and brand colors to maintain consistency.

**Deliverables:**
- High-resolution digital file compatible with billboard printing specifications.
- Consider mockups or visualizations for presentation purposes.

Please note that I have attached current logos/graphics that we would love to incorporate into the billboard as well as a picture of our current billboard. Our logo (Pat Greene Self Storage - PG navy.png) MUST be incorporated into the billboard. Also feel free to add any of the current descriptions from the picture of our current billboard into the design. Instead of using "Climate Controlled" use "Temperature Controlled". Thank you for your attention to these details. We look forward to reviewing your proposed design!

```html
<!DOCTYPE html>
<html lang="en">
<head>
<meta charset="utf-8">
<title>Pat Greene Billboard</title>
<link rel="stylesheet" href="https://fonts.googleapis.com/css2?family=Bebas+Neue&family=Montserrat:wght@800;900&family=Poppins:wght@600;700&display=swap">
<style>
  :root {
    --navy: #0f2a5e;
    --navy-deep: #0a1a3d;
    --tan: #9b7552;
    --blue: #1f5cc0;
    --white: #ffffff;
    --stage: #7f7f7f;
    --steel-light: #eef0f2;
    --steel: #b9bec4;
  }
  * { margin: 0; padding: 0; box-sizing: border-box; }
  html, body { width: 929px; height: 1200px; overflow: hidden; }
  body { background: var(--stage); position: relative; }

  .billboard {
    position: absolute; left: 20px; top: 378px;
    width: 889px; height: 445px;
    background: var(--white);
    overflow: hidden;
    box-shadow: 0 6px 18px rgba(0,0,0,.35);
  }
  .units-photo {
    position: absolute; right: 0; top: 0; width: 470px; height: 310px;
    background: linear-gradient(90deg, rgba(255,255,255,1) 0%, rgba(226,229,232,.9) 35%, var(--steel) 100%);
  }
  .doors-band {
    position: absolute; left: 0; right: 0; top: 307px; bottom: 0;
    background: linear-gradient(180deg, var(--navy-deep), #0c2150);
  }

  .brand {
    position: absolute; left: 45px; top: 42px;
    display: flex; align-items: center; gap: 12px;
    font-family: "Poppins", sans-serif; font-weight: 700;
    color: var(--navy); line-height: 1;
  }
  .brand-dot { width: 40px; height: 40px; border-radius: 50%; background: var(--navy); }
  .brand-name { font-size: 38px; letter-spacing: 1px; }
  .brand-sub { font-size: 15px; letter-spacing: 9px; margin-top: 6px; }

  .headline {
    position: absolute; left: 40px; top: 136px;
    font-family: "Bebas Neue", sans-serif; font-size: 108px;
    line-height: .9; color: var(--tan); letter-spacing: 0;
  }
  .tagline {
    position: absolute; left: 43px; top: 233px;
    font-family: "Montserrat", sans-serif; font-weight: 900;
    font-size: 33px; color: var(--navy); letter-spacing: -.3px;
  }

  .features {
    position: absolute; left: 43px; top: 281px; width: 565px; height: 64px;
    background: var(--tan); border-radius: 6px;
    display: flex; align-items: center; padding-left: 14px;
  }
  .feature {
    display: flex; gap: 6px; align-items: flex-start;
    font-family: "Poppins", sans-serif; font-weight: 600;
    font-size: 15.5px; line-height: 1.3; color: var(--white);
    padding-right: 14px; margin-right: 14px;
    border-right: 1px dashed rgba(255,255,255,.55);
  }
  .feature:last-child { border-right: none; }
  .feature svg { width: 12px; height: 12px; margin-top: 4px; flex: none; }

  .devices {
    position: absolute; left: 574px; top: 48px; width: 278px; height: 312px;
    border-radius: 14px;
    background: linear-gradient(160deg, #d8dbe0 0%, #1b2f5e 35%, #f4f5f7 70%, #c9cdd3 100%);
  }

  .address {
    position: absolute; left: 33px; top: 352px; width: 300px; height: 66px;
  }
  .address svg { position: absolute; inset: 0; }
  .address span {
    position: absolute; left: 38px; top: 0; height: 66px;
    display: flex; align-items: center;
    font-family: "Bebas Neue", sans-serif; font-size: 35px; color: var(--navy);
  }
  .phone {
    position: absolute; left: 340px; top: 364px; width: 221px; height: 44px;
    background: var(--blue);
    display: flex; align-items: center; gap: 8px; padding-left: 10px;
    font-family: "Bebas Neue", sans-serif; font-size: 35px; color: var(--white);
  }
  .phone svg { width: 24px; height: 24px; flex: none; }
  .website {
    position: absolute; left: 569px; top: 364px; width: 279px; height: 44px;
    background: var(--tan);
    display: flex; align-items: center; justify-content: center;
    font-family: "Poppins", sans-serif; font-weight: 700; font-size: 15.5px; color: var(--white);
  }
</style>
</head>
<body>
  <main class="billboard">
    <div class="units-photo" role="img" aria-label="Faded photo of a row of storage unit roll-up doors"></div>
    <div class="doors-band" role="img" aria-label="Navy-tinted photo of storage unit doors"></div>

    <div class="brand">
      <span class="brand-dot"></span>
      <div>
        <div class="brand-name">PAT GREENE</div>
        <div class="brand-sub">SELF STORAGE</div>
      </div>
    </div>

    <h1 class="headline">SELF STORAGE</h1>
    <p class="tagline">RENT ONLINE ANYTIME!</p>

    <ul class="features">
      <li class="feature"><svg viewBox="0 0 12 12"><circle cx="6" cy="6" r="6" fill="var(--navy)"/><path d="M3.2 6.2l1.9 1.8 3.7-3.9" stroke="#fff" stroke-width="1.5" fill="none"/></svg><span>Large/<br>Small Units</span></li>
      <li class="feature"><svg viewBox="0 0 12 12"><circle cx="6" cy="6" r="6" fill="var(--navy)"/><path d="M3.2 6.2l1.9 1.8 3.7-3.9" stroke="#fff" stroke-width="1.5" fill="none"/></svg><span>Temperature<br>Controlled</span></li>
      <li class="feature"><svg viewBox="0 0 12 12"><circle cx="6" cy="6" r="6" fill="var(--navy)"/><path d="M3.2 6.2l1.9 1.8 3.7-3.9" stroke="#fff" stroke-width="1.5" fill="none"/></svg><span>Covered Boat/<br>RV Parking</span></li>
    </ul>

    <div class="devices" role="img" aria-label="Tablet and phone showing the online storage rental website"></div>

    <div class="address">
      <svg viewBox="0 0 300 66" preserveAspectRatio="none"><polygon points="0,33 30,0 30,12 300,12 300,54 30,54 30,66" fill="#fff"/></svg>
      <span>215 MAPLE RIDGE DRIVE</span>
    </div>
    <div class="phone">
      <svg viewBox="0 0 24 24"><circle cx="12" cy="12" r="12" fill="#fff"/><path d="M8.2 6.5l2 .2.8 2.6-1.3 1.1c.7 1.5 1.8 2.6 3.2 3.3l1.1-1.3 2.6.8.2 2c-.3.9-1.2 1.5-2.2 1.4C10.2 16.2 7.6 13.6 7 9.1c-.1-1 .4-2.3 1.2-2.6z" fill="var(--blue)"/></svg>
      <span>478-555-0142</span>
    </div>
    <div class="website">www.patgreenestorage.com</div>
  </main>
</body>
</html>
```